Need a book cover design for a Vellora Book on Herbal Remedies

I need a book cover for my new ebook, here are the details:
Title: Meadow Tonics
Sub-Heading: Old Garden Wisdom Notes
Finding the Quiet Strength of the Wild for Daily Balance and Calm
Author: Mara Delacroix

```html
<!DOCTYPE html>
<html lang="en">
<head>
<meta charset="utf-8">
<title>Meadow Tonics — Mara Delacroix</title>
<link rel="stylesheet" href="https://fonts.googleapis.com/css2?family=Questrial&family=Crimson+Text:ital@0;1&display=swap">
<style>
  :root {
    --page-bg: #d9dadb;
    --cover-bg: #eceded;
    --band-orange: #c97822;
    --title-green: #4f9236;
    --title-orange: #dd8a1f;
    --ink: #1f1f1f;
    --white: #ffffff;
    --herb-green: #7e9a4e;
    --tea-amber: #c98a2a;
    --wood: #d8b98e;
  }
  * { margin: 0; padding: 0; box-sizing: border-box; }
  html, body {
    width: 1200px;
    height: 1200px;
    overflow: hidden;
    background: var(--page-bg);
  }
  .canvas {
    position: relative;
    width: 1200px;
    height: 1200px;
  }
  .book-cover {
    position: absolute;
    left: 230px;
    top: 30px;
    width: 740px;
    height: 1140px;
    background: var(--cover-bg);
    overflow: hidden;
  }
  .author-band {
    position: absolute;
    left: 40px;
    right: 40px;
    top: 48px;
    height: 64px;
    background: var(--band-orange);
    display: flex;
    align-items: center;
    justify-content: center;
  }
  .author-name {
    font-family: "Crimson Text", serif;
    font-size: 40px;
    letter-spacing: 1px;
    color: var(--white);
    text-transform: uppercase;
  }
  .title {
    position: absolute;
    left: 0;
    right: 0;
    top: 118px;
    text-align: center;
    font-family: "Questrial", sans-serif;
    font-weight: 400;
    text-transform: uppercase;
    line-height: 0.92;
  }
  .title-line { display: block; font-size: 136px; letter-spacing: -2px; }
  .title-line--green { color: var(--title-green); }
  .title-line--orange { color: var(--title-orange); }
  .subtitle {
    position: absolute;
    left: 30px;
    right: 30px;
    top: 400px;
    text-align: center;
    font-family: "Crimson Text", serif;
    font-style: italic;
    font-size: 27px;
    line-height: 1.25;
    color: var(--ink);
  }
  .herb-art {
    position: absolute;
    left: 0;
    right: 0;
    top: 490px;
    bottom: 0;
    background:
      radial-gradient(circle at 50% 38%, var(--tea-amber) 0 90px, var(--herb-green) 130px, rgba(236,237,237,0) 260px),
      radial-gradient(circle at 12% 92%, var(--wood) 0 90px, rgba(236,237,237,0) 200px),
      radial-gradient(circle at 88% 92%, #a0672c 0 70px, rgba(236,237,237,0) 170px),
      var(--cover-bg);
  }
</style>
</head>
<body>
  <div class="canvas">
    <section class="book-cover">
      <div class="author-band">
        <span class="author-name">Mara Delacroix</span>
      </div>
      <h1 class="title">
        <span class="title-line title-line--green">Meadow</span>
        <span class="title-line title-line--orange">Tonics</span>
      </h1>
      <p class="subtitle">Old Garden Wisdom Notes Finding the Quiet Strength<br>of the Wild for Daily Balance and Calm</p>
      <div class="herb-art" role="img" aria-label="Top-down photograph of a cup of herbal tea with chamomile flowers, surrounded by scattered dried herbs, blossoms, leaves, tea pearls and wooden spoons"></div>
    </section>
  </div>
</body>
</html>
```